Gala Event Program - Italian

Need a program with the exact same layout/structure as attached. The new theme for the event this year will be: Notte di Stelle Dorate, A Night of Golden Stars. The look that we are going for is Italian garden party. The page sizes should also be the same as previously - 8.5 X 11.

The image sizes relative to pring should remain roughly the same for the individual and group pages.

```html
<!DOCTYPE html>
<html lang="en">
<head>
<meta charset="utf-8">
<title>Notte di Stelle Dorate – Gala Program Spreads</title>
<link href="https://fonts.googleapis.com/css2?family=Michroma&family=Great+Vibes&family=Roboto:wght@400;700&display=swap" rel="stylesheet">
<style>
:root{
  --canvas:#a6a6a6;
  --terracotta:#cd8876;
  --rose:#c98472;
  --rose-light:#e3b3a3;
  --olive:#a9ad84;
  --olive-soft:#dfe0cc;
  --lemon:#f1e2a8;
  --ink:#1d1d1d;
  --white:#ffffff;
  --black:#000000;
}
*{margin:0;padding:0;box-sizing:border-box}
html,body{width:1200px;height:817px;overflow:hidden;background:var(--canvas)}
body{position:relative;font-family:'Roboto',sans-serif;color:var(--ink)}
.page{position:absolute;width:254px;height:330px;background:var(--white);overflow:hidden}
.page::after{content:"";position:absolute;inset:5px;border:1px solid var(--rose);pointer-events:none}
.row-top{top:61px}.row-bottom{top:427px}
.col-1{left:51px}.col-2{left:332px}.col-3{left:613px}.col-4{left:895px}
.caps{font-family:'Michroma',sans-serif;text-transform:uppercase;text-align:center;white-space:nowrap;
  background:linear-gradient(180deg,var(--rose-light),var(--rose) 60%,#b7705e);
  -webkit-background-clip:text;background-clip:text;color:transparent;line-height:1}
.script{font-family:'Great Vibes',cursive;text-align:center;line-height:1;color:var(--ink);white-space:nowrap}
.abs{position:absolute;left:0;right:0}
.backdrop{position:absolute;inset:5px;opacity:.6}

/* cover */
.cover::after{border:none}
.cover .field{position:absolute;inset:5px;background:var(--terracotta)}
.cover .wreath{position:absolute;left:47px;top:82px;width:160px;height:164px;border-radius:50%;
  background:radial-gradient(closest-side,rgba(241,226,168,.45),rgba(169,173,132,.35) 55%,rgba(205,136,118,0) 100%)}
.cover-title{position:absolute;left:0;right:0;top:152px;text-align:center;font-family:'Great Vibes',cursive;font-size:16px;line-height:1;color:var(--white)}
.cover-guild{position:absolute;left:0;right:0;top:175px;text-align:center;font-size:3.6px;letter-spacing:1px;color:var(--white)}

.blank{background:var(--black)}

/* festivities */
.festivities .backdrop{background:linear-gradient(160deg,#f6efe8 0%,#efe4d4 40%,#e9e2c6 70%,#f4eee5 100%)}
.schedule{position:absolute;left:0;right:0;top:74px;text-align:center}
.time{font-weight:700;font-size:10.5px;line-height:12px;margin-top:8px}
.item{font-size:7.2px;line-height:10.3px;margin-top:5px}
.item+.item{margin-top:0}

/* sponsor */
.sponsor::after{border:none}
.sponsor .field{position:absolute;inset:5px;background:linear-gradient(150deg,#cf8b78,#c98371 55%,#cf9380)}
.sponsor .caps{background:linear-gradient(180deg,#f6ddd3,#e9bfb0);-webkit-background-clip:text;background-clip:text}
.sponsor-mark{position:absolute;left:0;right:0;top:112px;display:flex;align-items:center;justify-content:center;gap:6px}
.sponsor-mark .dot{width:14px;height:14px;border-radius:50%;background:var(--white)}
.sponsor-mark span{font-family:'Michroma',sans-serif;font-size:11px;color:var(--white);letter-spacing:.5px}
.thanks{position:absolute;font-family:'Great Vibes',cursive;color:var(--white);line-height:1;white-space:nowrap}

/* inner pages */
.committee .backdrop{background:linear-gradient(170deg,#f7f2ee,#eee6dc 55%,#f3efe6)}
.bios .backdrop{background:linear-gradient(170deg,#f7f2ee,#eeeadc 60%,#f6efec)}
.juniors .backdrop{background:linear-gradient(170deg,#f7f3ee,#ece8dc 60%,#f6efec)}
.roster{position:absolute;left:77px;top:103px;list-style:none}
.roster li{font-size:7.4px;line-height:14.15px;display:flex;align-items:center;gap:5px}
.roster svg{width:6px;height:6px;flex:none}

.bio{position:absolute;font-size:4.3px;line-height:8.2px;text-align:justify;color:#333}
.portrait{position:absolute}
.portrait-frame{position:absolute;border:1px solid var(--rose)}

.group-photo{position:absolute;left:15px;top:73px;width:225px;height:149px;border:1px solid var(--rose);
  background:linear-gradient(180deg,#d6e3ef 0%,#e8eef0 35%,#a9ad84 60%,#b8a98e 80%,#9c8a74 100%)}
.caption{position:absolute;left:20px;right:21px;top:231px;font-size:7.2px;line-height:12.9px;text-align:center;color:#333}
.rule{position:absolute;left:94px;width:65px;top:294px;height:2px;background:var(--rose)}
</style>
</head>
<body>

<section class="page cover row-top col-1">
  <div class="field"></div>
  <div class="wreath" role="img" aria-label="Italian garden wreath of olive branches and lemon blossoms framing the title"></div>
  <div class="cover-title">Notte di Stelle Dorate</div>
  <div class="cover-guild">VIREO SYMPHONY GUILD</div>
</section>

<section class="page blank row-top col-2"></section>

<section class="page festivities row-top col-3">
  <div class="backdrop" role="img" aria-label="Faint photograph of an Italian hillside village with garden terraces by the sea"></div>
  <h2 class="caps abs" style="top:18px;font-size:20px">Evening</h2>
  <div class="script abs" style="top:40px;font-size:30px">Festivities</div>
  <div class="schedule">
    <p class="time">7:30 PM</p>
    <p class="item">Cocktail Reception (Cash Bar)</p>
    <p class="item">Heads and Tails Sales Open</p>
    <p class="item">Gold Grab Cupcake Sales Open</p>
    <p class="time">8:00 PM</p>
    <p class="item">Presentation of Belles and Beaux</p>
    <p class="time">9:15 PM</p>
    <p class="item">Heads and Tail</p>
    <p class="item">Dinner Immediately Following&nbsp; Heads and Tails</p>
    <p class="time">9:45 PM</p>
    <p class="item">Dancing</p>
    <p class="time">11:45 PM</p>
    <p class="item">Drawing for $1000 Gift Card</p>
    <p class="time">12:00 Midnight</p>
    <p class="item">Conclusion</p>
  </div>
</section>

<section class="page sponsor row-top col-4">
  <div class="field" role="img" aria-label="Faint terracotta-toned photograph of an Italian garden with lemon trees"></div>
  <h2 class="caps abs" style="top:18px;font-size:20px">Program</h2>
  <div class="script abs" style="top:38px;font-size:32px;color:#fff">Sponsor</div>
  <div class="sponsor-mark"><i class="dot"></i><span>MARLOW CONTROLS</span></div>
  <p class="thanks" style="left:15px;top:188px;font-size:21px">Special thanks to...</p>
  <p class="thanks" style="left:46px;top:226px;font-size:25px">Dylan Moreau</p>
  <p class="thanks" style="left:78px;top:265px;font-size:21px">For program design</p>
</section>

<section class="page committee row-bottom col-1">
  <div class="backdrop" role="img" aria-label="Faint photograph of a garden dinner table with wine glasses under olive trees"></div>
  <h2 class="caps abs" style="top:18px;font-size:19px;line-height:22px">Symphony<br>Ball</h2>
  <div class="script abs" style="top:66px;font-size:30px">Committee</div>
  <ul class="roster">
    <li><svg viewBox="0 0 10 10"><circle cx="5" cy="5" r="4.2" fill="none" stroke="#c98472" stroke-width="1.2"/><path d="M3 5.2l1.4 1.4L7.2 3.8" fill="none" stroke="#c98472" stroke-width="1.2"/></svg>Sofia Bellamy - Chair</li>
    <li><svg viewBox="0 0 10 10"><circle cx="5" cy="5" r="4.2" fill="none" stroke="#c98472" stroke-width="1.2"/><path d="M3 5.2l1.4 1.4L7.2 3.8" fill="none" stroke="#c98472" stroke-width="1.2"/></svg>Lena Whitford - President, Ex-officio</li>
    <li><svg viewBox="0 0 10 10"><circle cx="5" cy="5" r="4.2" fill="none" stroke="#c98472" stroke-width="1.2"/><path d="M3 5.2l1.4 1.4L7.2 3.8" fill="none" stroke="#c98472" stroke-width="1.2"/></svg>Maren Holt</li>
    <li><svg viewBox="0 0 10 10"><circle cx="5" cy="5" r="4.2" fill="none" stroke="#c98472" stroke-width="1.2"/><path d="M3 5.2l1.4 1.4L7.2 3.8" fill="none" stroke="#c98472" stroke-width="1.2"/></svg>Nora Quinlan</li>
    <li><svg viewBox="0 0 10 10"><circle cx="5" cy="5" r="4.2" fill="none" stroke="#c98472" stroke-width="1.2"/><path d="M3 5.2l1.4 1.4L7.2 3.8" fill="none" stroke="#c98472" stroke-width="1.2"/></svg>Ivy Pemberton</li>
    <li><svg viewBox="0 0 10 10"><circle cx="5" cy="5" r="4.2" fill="none" stroke="#c98472" stroke-width="1.2"/><path d="M3 5.2l1.4 1.4L7.2 3.8" fill="none" stroke="#c98472" stroke-width="1.2"/></svg>Carla Winslow</li>
    <li><svg viewBox="0 0 10 10"><circle cx="5" cy="5" r="4.2" fill="none" stroke="#c98472" stroke-width="1.2"/><path d="M3 5.2l1.4 1.4L7.2 3.8" fill="none" stroke="#c98472" stroke-width="1.2"/></svg>Tessa Rowe S</li>
    <li><svg viewBox="0 0 10 10"><circle cx="5" cy="5" r="4.2" fill="none" stroke="#c98472" stroke-width="1.2"/><path d="M3 5.2l1.4 1.4L7.2 3.8" fill="none" stroke="#c98472" stroke-width="1.2"/></svg>Jolie Marsh</li>
    <li><svg viewBox="0 0 10 10"><circle cx="5" cy="5" r="4.2" fill="none" stroke="#c98472" stroke-width="1.2"/><path d="M3 5.2l1.4 1.4L7.2 3.8" fill="none" stroke="#c98472" stroke-width="1.2"/></svg>Alma Reyes</li>
    <li><svg viewBox="0 0 10 10"><circle cx="5" cy="5" r="4.2" fill="none" stroke="#c98472" stroke-width="1.2"/><path d="M3 5.2l1.4 1.4L7.2 3.8" fill="none" stroke="#c98472" stroke-width="1.2"/></svg>Delia Fontaine</li>
    <li><svg viewBox="0 0 10 10"><circle cx="5" cy="5" r="4.2" fill="none" stroke="#c98472" stroke-width="1.2"/><path d="M3 5.2l1.4 1.4L7.2 3.8" fill="none" stroke="#c98472" stroke-width="1.2"/></svg>Pia Navarro</li>
    <li><svg viewBox="0 0 10 10"><circle cx="5" cy="5" r="4.2" fill="none" stroke="#c98472" stroke-width="1.2"/><path d="M3 5.2l1.4 1.4L7.2 3.8" fill="none" stroke="#c98472" stroke-width="1.2"/></svg>Claire Ashby</li>
    <li><svg viewBox="0 0 10 10"><circle cx="5" cy="5" r="4.2" fill="none" stroke="#c98472" stroke-width="1.2"/><path d="M3 5.2l1.4 1.4L7.2 3.8" fill="none" stroke="#c98472" stroke-width="1.2"/></svg>Greta Lindqvist</li>
    <li><svg viewBox="0 0 10 10"><circle cx="5" cy="5" r="4.2" fill="none" stroke="#c98472" stroke-width="1.2"/><path d="M3 5.2l1.4 1.4L7.2 3.8" fill="none" stroke="#c98472" stroke-width="1.2"/></svg>Wren Calloway A</li>
    <li><svg viewBox="0 0 10 10"><circle cx="5" cy="5" r="4.2" fill="none" stroke="#c98472" stroke-width="1.2"/><path d="M3 5.2l1.4 1.4L7.2 3.8" fill="none" stroke="#c98472" stroke-width="1.2"/></svg>Marisol Ortega</li>
  </ul>
</section>

<section class="page bios row-bottom col-2">
  <div class="backdrop" role="img" aria-label="Faint photograph of an Italian garden terrace with lanterns"></div>
  <h2 class="caps abs" style="top:18px;font-size:20px">Rowan</h2>
  <div class="script abs" style="top:39px;font-size:28px">Miles Hartwell</div>
  <p class="bio" style="left:15px;width:116px;top:76px">Rowan Miles Hartwell, 18, is the son of Mr. &amp; Mrs. Victor Hartwell. He is the grandson of Mr. &amp; Mrs. Owen Pryce, Mrs. Helen Doyle, and the late Mr. Carl Hartwell. Rowan is a senior at Meridian Preparatory School. He is a four-year member of the Meridian varsity basketball team. He has earned community service awards for Texas Scholars. He will graduate with enough dual credit hours to begin his sophomore year in college. He plans to attend Westfield College in the fall and major in Business.</p>
  <div class="portrait-frame" style="left:140px;top:71px;width:97px;height:89px"></div>
  <div class="portrait" style="left:146px;top:74px;width:97px;height:89px;background:linear-gradient(180deg,#b9a79c,#8b7f7a)" role="img" aria-label="Portrait photo of a young man in a grey suit before a brick wall"></div>
  <h2 class="caps" style="position:absolute;left:33px;top:164px;font-size:20px">Lucia</h2>
  <div class="script" style="position:absolute;left:14px;top:186px;font-size:28px;text-align:left">Noelle Brandt</div>
  <div class="portrait-frame" style="left:21px;top:222px;width:96px;height:92px"></div>
  <div class="portrait" style="left:17px;top:225px;width:94px;height:90px;background:linear-gradient(180deg,#c9b79a,#a7836c 60%,#e9c7d4)" role="img" aria-label="Portrait photo of a young woman in a pink dress outdoors"></div>
  <p class="bio" style="left:126px;width:117px;top:227px">Lucia Noelle Brandt, 17, is the daughter of Mr. &amp; Mrs. Simon Gale and Mr. &amp; Mrs. Paul Brandt. She is the granddaughter of Mr. &amp; Mrs. Martin Ellery, Mr. &amp; Mrs. Roger Brandt, Mr. &amp; Mrs. Neil Sutter, and Mr. Grant Oakley. Lucia attends Meridian Preparatory School and is currently #3 in her class. She is a member of the National Honor Society and Texas Scholars. She is a three-year letterman in Varsity volleyball. Throughout volleyball, she was awarded Academic All-District, Second team All-State Academic, Newcomer of the Year, Offensive MVP, and First Team All-District.</p>
</section>

<section class="page juniors row-bottom col-3">
  <div class="backdrop" role="img" aria-label="Faint photograph of an Italian garden venue"></div>
  <div class="script abs" style="top:20px;font-size:36px">Juniors</div>
  <div class="group-photo" role="img" aria-label="Group photo of the juniors in black outfits in a garden courtyard"></div>
  <p class="caption">Left to right: Amara Lind, Jordan Blake, Rosa Penn, Hallie Vance, Eden Whitford, Elise Bellamy, Tristan Gale, Gabriel Rios, Toby Stroud, Bria Dale, Emery Colt, Piper Jett, Kira Umber, Aubrey Dunmore, Daria Valle, Maddie Dorn</p>
  <div class="rule"></div>
</section>

</body>
</html>
```